Business Card Design

We need a new business card design for a company based in Larkmont, OR. We provide business consulting services in the information technology / services space. We like variations of the color blue, aqua, black, light tan, and white. Would like "cool" tones. The design should clearly communicate professionalism. Think outside the box - we don't want something "typical". Our company name is "Vantrell Advisory, LLC".
Updates

Thank you all for your submissions. We have seen some very creative and inspired designs. We have made a decision and will be moving forward with that design. Appreciate all of the hard work.

Industry/Entity Type

Information Technology

Contact Information for Business Card

Denise Harlow Trumbey
482 West Maple Ridge Dr.
Larkmont, OR 76185

```html
<!DOCTYPE html>
<html lang="en">
<head>
<meta charset="utf-8">
<title>Vantrell Advisory, LLC — Business Card</title>
<link rel="stylesheet" href="https://fonts.googleapis.com/css2?family=Montserrat:wght@400;600&display=swap">
<style>
  :root {
    --backdrop: #9dc0cc;
    --card-white: #f1f3f4;
    --band-teal: #3c9cba;
    --corner-teal: #1d6a86;
    --divider: #f4f6f7;
    --ink: #15242c;
    --ink-soft: #2b3a42;
  }
  html, body {
    margin: 0;
    width: 1200px;
    height: 873px;
    overflow: hidden;
    background: var(--backdrop);
  }
  .canvas {
    position: relative;
    width: 1200px;
    height: 873px;
    display: flex;
    align-items: center;
    justify-content: center;
  }
  .business-card {
    position: relative;
    width: 700px;
    height: 400px;
    background: var(--card-white);
    overflow: hidden;
    box-shadow: 0 18px 40px rgba(20, 60, 75, 0.25);
  }
  .card-shapes {
    position: absolute;
    inset: 0;
    width: 100%;
    height: 100%;
  }
  .company-name {
    position: absolute;
    left: 200px;
    top: 128px;
    margin: 0;
    font-family: "Montserrat", sans-serif;
    font-weight: 600;
    font-size: 34px;
    letter-spacing: 0.2px;
    color: var(--ink);
    white-space: nowrap;
  }
  .contact {
    position: absolute;
    left: 200px;
    top: 232px;
    margin: 0;
    font-family: "Montserrat", sans-serif;
    font-style: normal;
    font-weight: 400;
    font-size: 22px;
    line-height: 34px;
    color: var(--ink-soft);
    white-space: nowrap;
  }
  .contact-line { display: block; }
  .contact-name { margin-bottom: 8px; }
</style>
</head>
<body>
  <main class="canvas">
    <article class="business-card">
      <svg class="card-shapes" viewBox="0 0 700 400" aria-hidden="true">
        <rect class="top-band" x="0" y="0" width="700" height="185" fill="var(--band-teal)"/>
        <polygon class="corner-facet" points="0,0 150,185 0,400" fill="var(--corner-teal)"/>
        <line class="facet-divider" x1="0" y1="0" x2="150" y2="185" stroke="var(--divider)" stroke-width="6"/>
      </svg>
      <h1 class="company-name">Vantrell Advisory, LLC</h1>
      <address class="contact">
        <span class="contact-line contact-name">Denise Harlow Trumbey</span>
        <span class="contact-line">482 West Maple Ridge Dr.</span>
        <span class="contact-line">Larkmont, OR 76185</span>
      </address>
    </article>
  </main>
</body>
</html>
```